Pebble and Pine App design

I need a full app design, colours, images, fonts, and a mock up design of the app to bring to the developer.

Pebble and Pine is a free app that allows cafes, independent cafe and chains of cafes to let their customers know what the soup of the day and what specials they have on that day through the app. Each cafe will have a profile which they can upload the Pebble and Pine daily.

The user home screen will include google maps showing their location with the registered cafes and eateries around them. including a list of the cafe and distances below. as seen in attachment.

Target Market(s)

Cafes , anyone who enjoys eating soups and off local cafe specials boards

Requirements
Must have
• I would like a complete app design based on the attached images.

```html
<!DOCTYPE html>
<html lang="en">
<head>
<meta charset="utf-8">
<title>Pebble and Pine – App screens</title>
<link href="https://fonts.googleapis.com/css2?family=DM+Sans:wght@400;500;600;700&display=swap" rel="stylesheet">
<style>
:root{
  --canvas:#e1e2e1;
  --screen:#ffffff;
  --ink:#1d2220;
  --muted:#a3a8a6;
  --line:#eceeed;
  --green:#7cc394;
  --green-soft:rgba(124,195,148,.28);
  --green-text:#5aae72;
  --red:#ec4c4c;
  --star:#f3b63f;
  --map-a:#f5f6f5;
  --map-b:#e6e8e7;
}
*{box-sizing:border-box;margin:0;padding:0}
html,body{width:786px;height:1200px;overflow:hidden}
body{background:var(--canvas);font-family:"DM Sans",sans-serif;color:var(--ink);position:relative}
ul{list-style:none}
.screen{position:absolute;width:170px;height:367px;background:var(--screen);border-radius:12px;overflow:hidden}
.s-list{left:203px;top:30px}
.s-map{left:413px;top:30px;border-radius:0}
.s-fav{left:203px;top:412px}
.s-dish{left:413px;top:412px}
.s-place{left:203px;top:794px}

.screen-title{position:absolute;left:11px;top:28px;font-size:11px;font-weight:600;letter-spacing:-.1px}
.tabs{position:absolute;left:11px;right:11px;top:54px;height:25px;display:flex;gap:5px}
.tab{flex:1;border:1px solid var(--line);border-radius:6px;display:flex;align-items:center;justify-content:center;gap:4px;font-size:5px;font-weight:500}
.tab svg{width:8px;height:6px}
.tab.active{background:var(--green);border-color:var(--green);color:#fff}

.dishes{position:absolute;left:11px;right:11px;top:97px}
.dish{display:flex;align-items:flex-start;height:47px}
.thumb{width:36px;height:36px;border-radius:8px;position:relative;flex:none}
.likes{position:absolute;left:17px;bottom:3px;background:#fff;border-radius:4px;font-size:3.4px;padding:1px 2px;font-weight:600}
.likes b{color:var(--red)}
.dish-info{flex:1;padding-left:7px;padding-top:5px}
.dish-name{font-size:5.3px;font-weight:600}
.dish-from{font-size:3.8px;margin-top:2px}
.dish-from span{color:var(--muted)}
.price{font-size:4.2px;color:var(--green-text);margin-top:7px;font-weight:500}
.fav-count{font-size:3.8px;margin-top:5px}
.fav-count b{color:var(--red)}
.heart{width:7px;height:7px;margin-top:5px}
.dot{width:3.5px;height:3.5px;border-radius:50%;margin-top:8px;margin-right:1px;background:var(--green)}
.dot.red{background:var(--red)}

.nav{position:absolute;left:0;right:0;top:325px;height:42px;background:#fff;display:flex;justify-content:space-around;padding:4px 12px 0}
.nav-item{width:10px;display:flex;flex-direction:column;align-items:center;gap:3px}
.nav-item svg{width:9px;height:9px}
.nav-item.on::after{content:"";width:2px;height:2px;border-radius:50%;background:var(--green)}
.home-bar{position:absolute;left:48px;bottom:7px;width:74px;height:2px;border-radius:1px;background:#d6d8d7}

.ph-chowder{background:radial-gradient(circle at 50% 50%,#f1c93a 0 38%,#e7dbb5 40% 46%,#9b6a3f 48%,#6c4a2c)}
.ph-noodle{background:radial-gradient(circle at 45% 50%,#d8b447 0 30%,#4a6b4a 34% 55%,#c8cac6 60%)}
.ph-onion{background:radial-gradient(circle at 50% 50%,#d9692f 0 36%,#ece3d6 40% 48%,#7b5a44 52%)}
.ph-torts{background:radial-gradient(circle at 55% 48%,#e07a33 0 26%,#eeeae2 30% 45%,#7f93a3 50%)}
.ph-bisque{background:radial-gradient(circle at 50% 50%,#d45b2c 0 34%,#e7c9a2 40% 48%,#caa07a 55%)}
.ph-cafe{background:linear-gradient(180deg,#3b3f36 0%,#5d4a35 45%,#2f3a2e 100%)}
.ph-cafe2{background:linear-gradient(180deg,#6a5038 0%,#3f3a2f 55%,#2c2b24 100%)}
.ph-cafe3{background:linear-gradient(180deg,#5b6a6c 0%,#334044 60%,#273032 100%)}
.ph-cafe4{background:linear-gradient(180deg,#b7aa98 0%,#6e5d4b 60%,#3a3128 100%)}
.ph-fritter{background:radial-gradient(circle at 45% 50%,#ee8a3a 0 40%,#f1ede6 48%)}
.ph-pancake{background:radial-gradient(circle at 50% 55%,#8d5a36 0 40%,#e9e1d4 48%)}

.map{position:absolute;inset:0 0 42px 0;background:linear-gradient(160deg,var(--map-a) 0%,var(--map-b) 45%,#eef0ef 70%,var(--map-a) 100%)}
.map-pins{position:absolute;left:0;top:0;width:170px;height:200px}
.map-card{position:absolute;top:181px;width:134px;height:124px;background:#fff;border-radius:7px;padding:7px;box-shadow:0 4px 14px rgba(0,0,0,.06)}
.map-card.first{left:7px}
.map-card.second{left:149px}
.card-photo{height:46px;border-radius:6px;position:relative}
.card-photo .name{position:absolute;left:7px;bottom:6px;color:#fff;font-size:5px;font-weight:600;white-space:nowrap}
.rating{position:absolute;right:5px;bottom:5px;background:#fff;border-radius:3px;font-size:3.4px;padding:1px 2px;font-weight:600}
.rating b{color:var(--star)}
.card-cols{display:flex;margin-top:8px}
.card-cols div{flex:1}
.label{font-size:3.4px;color:var(--muted)}
.value{font-size:4px;color:var(--green-text);margin-top:2px;white-space:nowrap}
.card-meta{display:flex;margin-top:9px}
.card-meta span{flex:1;font-size:3.8px;display:flex;align-items:center;gap:2px;white-space:nowrap}
.card-meta svg{width:4px;height:4px;flex:none}
.btn{margin-top:9px;height:21px;border:1px solid var(--line);border-radius:6px;display:flex;align-items:center;justify-content:center;font-size:4.6px;font-weight:500}

.topbar{position:absolute;left:11px;right:11px;top:30px;display:flex;justify-content:space-between;align-items:center}
.topbar svg{width:7px;height:7px}
.hero-dish{position:absolute;left:53px;top:51px;width:63px;height:63px;border-radius:16px}
.hero-dish::after{content:"";position:absolute;right:3px;bottom:-2px;width:7px;height:7px;border-radius:50%;background:var(--green);border:1.2px solid #fff}
.dish-title{position:absolute;left:0;right:0;top:119px;text-align:center;font-size:11px;font-weight:600}
.row-head{position:absolute;left:11px;right:11px;display:flex;justify-content:space-between;font-size:4.2px;color:var(--muted);font-weight:500}
.row-head .price{margin:0}
.primary{position:absolute;left:11px;right:11px;top:155px;height:46px;border-radius:7px}
.primary .name{position:absolute;left:7px;bottom:6px;color:#fff;font-size:5px;font-weight:600}
.others{position:absolute;left:11px;right:11px;top:222px}
.other{display:flex;height:44px}
.other .thumb{width:72px;height:36px}
.other .likes{left:auto;right:4px}
.other .likes b{color:var(--star)}

.cover{position:absolute;left:11px;right:11px;top:52px;height:72px;border-radius:8px}
.cover .rating{left:7px;right:auto;bottom:5px}
.place-name{position:absolute;left:11px;top:128px;font-size:11.5px;font-weight:700}
.address{position:absolute;left:11px;top:145px;font-size:4.2px;color:var(--muted)}
.directions{position:absolute;left:11px;top:153px;font-size:4.6px;color:var(--green-text);font-weight:500;display:flex;gap:2px;align-items:center}
.directions svg{width:4px;height:4px}
.section-label{position:absolute;left:11px;font-size:4.3px;color:var(--muted);font-weight:500}
.about{position:absolute;left:11px;right:11px;top:179px;font-size:4.3px;line-height:1.9}
.soup-row{position:absolute;left:11px;top:235px;display:flex;gap:8px}
.soup-card{width:60px;height:74px;border-radius:8px;position:relative;flex:none}
.soup-card .tag{position:absolute;left:5px;bottom:21px;background:#fff;border-radius:3px;font-size:3.2px;padding:1px 2px;font-weight:600;line-height:1}
.soup-card .name{position:absolute;left:5px;right:4px;bottom:5px;color:#fff;font-size:4.4px;font-weight:600;line-height:1.25}
.special-row{position:absolute;left:11px;top:332px;display:flex;gap:10px}
.special{display:flex;gap:7px;width:85px;flex:none}
.special .thumb{width:36px;height:36px}
.special .dish-name{margin-top:4px;line-height:1.2}
.special .price{margin-top:5px}
</style>
</head>
<body>

<!-- Dish list -->
<section class="screen s-list">
  <h1 class="screen-title">Pebble and Pine</h1>
  <div class="tabs">
    <div class="tab active"><svg viewBox="0 0 8 6" fill="none" stroke="currentColor" stroke-width=".7"><path d="M.5 2.5h7M1 2.5a3 3 0 006 0M3 .3v1.2M4 .3v1.2M5 .3v1.2M2.5 5.6h3"/></svg>Soups</div>
    <div class="tab"><svg viewBox="0 0 8 6" fill="none" stroke="currentColor" stroke-width=".7"><path d="M.5 5h7M1 5a3 3 0 016 0M4 1.5v.5M1 .5l1 1M7 .5l-1 1"/></svg>Specials</div>
  </div>
  <ul class="dishes">
    <li class="dish"><div class="thumb ph-chowder" role="img" aria-label="Bowl of shrimp and corn chowder"><span class="likes"><b>♥</b> 236</span></div><div class="dish-info"><p class="dish-name">Shrimp and corn chowder</p><p class="dish-from"><span>from</span> Flint Kettle Cafe</p><p class="price">$30.00</p></div><svg class="heart" viewBox="0 0 10 10" fill="none" stroke="#1d2220" stroke-width=".9"><path d="M5 8.6 1.3 5A2.2 2.2 0 015 2.3 2.2 2.2 0 018.7 5z"/></svg></li>
    <li class="dish"><div class="thumb ph-noodle" role="img" aria-label="Bowl of chicken noodle soup"><span class="likes"><b>♥</b> 12</span></div><div class="dish-info"><p class="dish-name">Chicken noodle soup</p><p class="dish-from"><span>from</span> Cafe Lumo</p><p class="price">$56.80</p></div><svg class="heart" viewBox="0 0 10 10" fill="#ec4c4c"><path d="M5 8.6 1.3 5A2.2 2.2 0 015 2.3 2.2 2.2 0 018.7 5z"/></svg></li>
    <li class="dish"><div class="thumb ph-onion" role="img" aria-label="Bowl of French onion soup"><span class="likes"><b>♥</b> 763</span></div><div class="dish-info"><p class="dish-name">French onion soup</p><p class="dish-from"><span>from</span> Café des Tilleuls</p><p class="price">$25.99</p></div><svg class="heart" viewBox="0 0 10 10" fill="none" stroke="#1d2220" stroke-width=".9"><path d="M5 8.6 1.3 5A2.2 2.2 0 015 2.3 2.2 2.2 0 018.7 5z"/></svg></li>
    <li class="dish"><div class="thumb ph-torts" role="img" aria-label="Tomato soup with cheese torts"><span class="likes"><b>♥</b> 29</span></div><div class="dish-info"><p class="dish-name">Tomato and cheese torts</p><p class="dish-from"><span>from</span> Flint Kettle Cafe</p><p class="price">$12.00</p></div><svg class="heart" viewBox="0 0 10 10" fill="none" stroke="#1d2220" stroke-width=".9"><path d="M5 8.6 1.3 5A2.2 2.2 0 015 2.3 2.2 2.2 0 018.7 5z"/></svg></li>
    <li class="dish"><div class="thumb ph-bisque" role="img" aria-label="Bowl of lobster bisque"><span class="likes"><b>♥</b> 83</span></div><div class="dish-info"><p class="dish-name">Lobster bisque</p><p class="dish-from"><span>from</span> Café des Tilleuls</p><p class="price">$16.25</p></div><svg class="heart" viewBox="0 0 10 10" fill="#ec4c4c"><path d="M5 8.6 1.3 5A2.2 2.2 0 015 2.3 2.2 2.2 0 018.7 5z"/></svg></li>
  </ul>
  <nav class="nav">
    <span class="nav-item"><svg viewBox="0 0 10 10" fill="none" stroke="#1d2220" stroke-width=".9"><path d="M1.5 4.5 5 1.5l3.5 3V9h-7zM4 9V6.5h2V9"/></svg></span>
    <span class="nav-item"><svg viewBox="0 0 10 10" fill="none" stroke="#1d2220" stroke-width=".9"><circle cx="4.3" cy="4.3" r="3"/><path d="m6.6 6.6 2.4 2.4"/></svg></span>
    <span class="nav-item on"><svg viewBox="0 0 10 10" fill="none" stroke="#7cc394" stroke-width=".9"><path d="M.8 5h8.4M1.5 5a3.5 3.5 0 007 0M3.5 1v2M5 1v2M6.5 1v2M3 9.2h4"/></svg></span>
    <span class="nav-item"><svg viewBox="0 0 10 10" fill="none" stroke="#1d2220" stroke-width=".9"><path d="M5 8.6 1.3 5A2.2 2.2 0 015 2.3 2.2 2.2 0 018.7 5z"/></svg></span>
    <span class="nav-item"><svg viewBox="0 0 10 10" fill="none" stroke="#1d2220" stroke-width=".9"><circle cx="5" cy="5" r="1.5"/><circle cx="5" cy="5" r="3.6" stroke-dasharray="1.4 .8"/></svg></span>
  </nav>
  <span class="home-bar"></span>
</section>

<!-- Map home -->
<section class="screen s-map">
  <div class="map" role="img" aria-label="Street map of the neighbourhood around the user"></div>
  <svg class="map-pins" viewBox="0 0 170 200" aria-label="Nearby cafe markers and current location">
    <g fill="var(--green-soft)">
      <circle cx="37" cy="60" r="5"/>
      <circle cx="58" cy="79" r="5"/>
      <circle cx="110" cy="14" r="5"/>
      <circle cx="159" cy="103" r="5"/>
      <circle cx="67" cy="153" r="5"/>
      <circle cx="112" cy="91" r="12"/>
    </g>
    <g fill="var(--green)">
      <circle cx="37" cy="60" r="2"/>
      <circle cx="58" cy="79" r="2"/>
      <circle cx="110" cy="14" r="2"/>
      <circle cx="159" cy="103" r="2"/>
      <circle cx="67" cy="153" r="2"/>
    </g>
    <circle cx="112" cy="91" r="2.4" fill="var(--green)" stroke="#fff" stroke-width="1"/>
  </svg>
  <article class="map-card first">
    <div class="card-photo ph-cafe2" role="img" aria-label="Terrace of Café des Tilleuls"><span class="name">Café des Tilleuls</span><span class="rating"><b>★</b> 4.8</span></div>
    <div class="card-cols"><div><p class="label">Soup</p><p class="value">French onion soup</p></div><div><p class="label">Special</p><p class="value">Lobster bisque</p></div></div>
    <div class="card-meta"><span><svg viewBox="0 0 4 4" fill="none" stroke="#1d2220" stroke-width=".4"><path d="M2 3.8S.6 2.4.6 1.5a1.4 1.4 0 012.8 0C3.4 2.4 2 3.8 2 3.8z"/></svg>12 kilometers away</span><span><svg viewBox="0 0 4 4" fill="none" stroke="#1d2220" stroke-width=".4"><circle cx="2" cy="2" r="1.7"/><path d="M2 1v1l.7.5"/></svg>9:00am - 10:30pm</span></div>
    <div class="btn">View Details</div>
  </article>
  <article class="map-card second">
    <div class="card-photo ph-cafe" role="img" aria-label="Dining room of Flint Kettle Cafe"><span class="name">Flint Kettle Cafe</span><span class="rating"><b>★</b> 4.5</span></div>
    <div class="card-cols"><div><p class="label">Soup</p><p class="value">Shrimp and corn chowder</p></div><div><p class="label">Special</p><p class="value">Tomato and cheese torts</p></div></div>
    <div class="card-meta"><span><svg viewBox="0 0 4 4" fill="none" stroke="#1d2220" stroke-width=".4"><path d="M2 3.8S.6 2.4.6 1.5a1.4 1.4 0 012.8 0C3.4 2.4 2 3.8 2 3.8z"/></svg>24 kilometers away</span><span><svg viewBox="0 0 4 4" fill="none" stroke="#1d2220" stroke-width=".4"><circle cx="2" cy="2" r="1.7"/><path d="M2 1v1l.7.5"/></svg>7:00am - 5:30pm</span></div>
    <div class="btn">View Details</div>
  </article>
  <nav class="nav">
    <span class="nav-item on"><svg viewBox="0 0 10 10" fill="none" stroke="#7cc394" stroke-width=".9"><path d="M1.5 4.5 5 1.5l3.5 3V9h-7zM4 9V6.5h2V9"/></svg></span>
    <span class="nav-item"><svg viewBox="0 0 10 10" fill="none" stroke="#1d2220" stroke-width=".9"><circle cx="4.3" cy="4.3" r="3"/><path d="m6.6 6.6 2.4 2.4"/></svg></span>
    <span class="nav-item"><svg viewBox="0 0 10 10" fill="none" stroke="#1d2220" stroke-width=".9"><path d="M.8 5h8.4M1.5 5a3.5 3.5 0 007 0M3.5 1v2M5 1v2M6.5 1v2M3 9.2h4"/></svg></span>
    <span class="nav-item"><svg viewBox="0 0 10 10" fill="none" stroke="#1d2220" stroke-width=".9"><path d="M5 8.6 1.3 5A2.2 2.2 0 015 2.3 2.2 2.2 0 018.7 5z"/></svg></span>
    <span class="nav-item"><svg viewBox="0 0 10 10" fill="none" stroke="#1d2220" stroke-width=".9"><circle cx="5" cy="5" r="1.5"/><circle cx="5" cy="5" r="3.6" stroke-dasharray="1.4 .8"/></svg></span>
  </nav>
  <span class="home-bar"></span>
</section>

<!-- Favourites -->
<section class="screen s-fav">
  <h1 class="screen-title">Favourites</h1>
  <div class="tabs">
    <div class="tab"><svg viewBox="0 0 8 6" fill="none" stroke="currentColor" stroke-width=".7"><path d="M.5 2.5h7M1 2.5a3 3 0 006 0M3 .3v1.2M4 .3v1.2M5 .3v1.2M2.5 5.6h3"/></svg>Soups</div>
    <div class="tab active"><svg viewBox="0 0 8 6" fill="none" stroke="currentColor" stroke-width=".7"><path d="M.5 5h7M1 5a3 3 0 016 0M4 1.5v.5M1 .5l1 1M7 .5l-1 1"/></svg>Specials</div>
  </div>
  <ul class="dishes">
    <li class="dish"><div class="thumb ph-noodle" role="img" aria-label="Bowl of chicken noodle soup"></div><div class="dish-info"><p class="dish-name">Chicken noodle soup</p><p class="dish-from"><span>from</span> Cafe Lumo</p><p class="fav-count"><b>♥</b> 12</p></div><span class="dot red"></span></li>
    <li class="dish"><div class="thumb ph-bisque" role="img" aria-label="Bowl of lobster bisque"></div><div class="dish-info"><p class="dish-name">Lobster bisque</p><p class="dish-from"><span>from</span> Café des Tilleuls</p><p class="fav-count"><b>♥</b> 83</p></div><span class="dot"></span></li>
    <li class="dish"><div class="thumb ph-torts" role="img" aria-label="Tomato soup with cheese torts"></div><div class="dish-info"><p class="dish-name">Tomato and cheese torts</p><p class="dish-from"><span>from</span> Flint Kettle Cafe</p><p class="fav-count"><b>♥</b> 29</p></div><span class="dot red"></span></li>
    <li class="dish"><div class="thumb ph-chowder" role="img" aria-label="Bowl of shrimp and corn chowder"></div><div class="dish-info"><p class="dish-name">Shrimp and corn chowder</p><p class="dish-from"><span>from</span> Flint Kettle Cafe</p><p class="fav-count"><b>♥</b> 236</p></div><span class="dot"></span></li>
    <li class="dish"><div class="thumb ph-onion" role="img" aria-label="Bowl of French onion soup"></div><div class="dish-info"><p class="dish-name">French onion soup</p><p class="dish-from"><span>from</span> Café des Tilleuls</p><p class="fav-count"><b>♥</b> 763</p></div><span class="dot"></span></li>
  </ul>
  <nav class="nav">
    <span class="nav-item"><svg viewBox="0 0 10 10" fill="none" stroke="#1d2220" stroke-width=".9"><path d="M1.5 4.5 5 1.5l3.5 3V9h-7zM4 9V6.5h2V9"/></svg></span>
    <span class="nav-item"><svg viewBox="0 0 10 10" fill="none" stroke="#1d2220" stroke-width=".9"><circle cx="4.3" cy="4.3" r="3"/><path d="m6.6 6.6 2.4 2.4"/></svg></span>
    <span class="nav-item"><svg viewBox="0 0 10 10" fill="none" stroke="#1d2220" stroke-width=".9"><path d="M.8 5h8.4M1.5 5a3.5 3.5 0 007 0M3.5 1v2M5 1v2M6.5 1v2M3 9.2h4"/></svg></span>
    <span class="nav-item on"><svg viewBox="0 0 10 10" fill="none" stroke="#7cc394" stroke-width=".9"><path d="M5 8.6 1.3 5A2.2 2.2 0 015 2.3 2.2 2.2 0 018.7 5z"/></svg></span>
    <span class="nav-item"><svg viewBox="0 0 10 10" fill="none" stroke="#1d2220" stroke-width=".9"><circle cx="5" cy="5" r="1.5"/><circle cx="5" cy="5" r="3.6" stroke-dasharray="1.4 .8"/></svg></span>
  </nav>
  <span class="home-bar"></span>
</section>

<!-- Dish detail -->
<section class="screen s-dish">
  <div class="topbar">
    <svg viewBox="0 0 8 8" fill="none" stroke="#1d2220" stroke-width="1"><path d="M5 1.5 2.5 4 5 6.5"/></svg>
    <svg viewBox="0 0 10 10" fill="#ec4c4c"><path d="M5 9 1 5.1A2.4 2.4 0 015 2.1a2.4 2.4 0 014 3z"/></svg>
  </div>
  <div class="hero-dish ph-chowder" role="img" aria-label="Bowl of shrimp and corn chowder"></div>
  <h1 class="dish-title">Shrimp and corn chowder</h1>
  <div class="row-head" style="top:147px"><span>Primary establishment</span><span class="price">$30.00</span></div>
  <div class="primary ph-cafe" role="img" aria-label="Dining room of Flint Kettle Cafe"><span class="name">Flint Kettle Cafe</span><span class="rating"><b>★</b> 4.5</span></div>
  <div class="row-head" style="top:213px"><span>Other establishments</span></div>
  <ul class="others">
    <li class="other"><div class="thumb ph-cafe2" role="img" aria-label="Terrace of Café des Tilleuls"><span class="likes"><b>★</b> 4.5</span></div><div class="dish-info"><p class="dish-name">Café des Tilleuls</p><p class="dish-from"><span>12 kilometers away</span></p><p class="price">$28.00</p></div></li>
    <li class="other"><div class="thumb ph-cafe3" role="img" aria-label="Interior of Marlowe's Place"><span class="likes"><b>★</b> 3.9</span></div><div class="dish-info"><p class="dish-name">Marlowe's Place</p><p class="dish-from"><span>27 kilometers away</span></p><p class="price">$22.65</p></div></li>
    <li class="other"><div class="thumb ph-cafe4" role="img" aria-label="Counter of Marlowe's Place"><span class="likes"><b>★</b> 4.8</span></div><div class="dish-info"><p class="dish-name">Marlowe's Place</p><p class="dish-from"><span>4 kilometers away</span></p><p class="price">$34.00</p></div></li>
  </ul>
</section>

<!-- Establishment profile -->
<section class="screen s-place">
  <div class="topbar" style="top:32px">
    <svg viewBox="0 0 8 8" fill="none" stroke="#1d2220" stroke-width="1"><path d="M5 1.5 2.5 4 5 6.5"/></svg>
  </div>
  <div class="cover ph-cafe" role="img" aria-label="Dining room of Flint Kettle Cafe"><span class="rating"><b>★</b> 4.5</span></div>
  <h1 class="place-name">Flint Kettle Cafe</h1>
  <p class="address">14 Rue des Ormes, 75007 Paris, France</p>
  <p class="directions"><svg viewBox="0 0 4 4" fill="none" stroke="currentColor" stroke-width=".4"><path d="M3.7.3.3 1.8l1.5.5.5 1.5z"/></svg>Get directions</p>
  <p class="section-label" style="top:169px">About establishment</p>
  <p class="about">Flint Kettle Cafe is a fine soup house founded in 2010 by Louis Marchetti - best French chef in 2011 - and Owen Hale. Its soups are being served in its seven specialty establishments in Paris and Geneva.</p>
  <p class="section-label" style="top:225px">Soups</p>
  <div class="soup-row">
    <div class="soup-card ph-chowder" role="img" aria-label="Shrimp and corn chowder"><span class="tag">$30.00</span><span class="name">Shrimp and corn chowder</span></div>
    <div class="soup-card ph-torts" role="img" aria-label="Tomato and cheese torts"><span class="tag">$12.00</span><span class="name">Tomato and cheese torts</span></div>
    <div class="soup-card ph-noodle" role="img" aria-label="Chicken noodle soup"><span class="tag">$56.80</span><span class="name">Chicken noodle soup</span></div>
  </div>
  <p class="section-label" style="top:322px">Specials</p>
  <div class="special-row">
    <div class="special"><div class="thumb ph-fritter" role="img" aria-label="Sweet potato fritters"></div><div><p class="dish-name">Sweet potato fritters</p><p class="price">$42.00</p></div></div>
    <div class="special"><div class="thumb ph-pancake" role="img" aria-label="Banana oatmeal pancakes"></div><div><p class="dish-name">Banana oat-meal panca...</p><p class="price">$12.99</p></div></div>
  </div>
</section>

</body>
</html>
```